Allied Health team of Physiotherapists & Occupational Therapists seek a business card design

We have our new logo, we now need our new business cards and stationary. Blossom: Lymphoedema & Women's Clinic is seeking a generic card design to represent our whole team and individual cards for each therapist that incorporates our new logo to communicate our holistic approach that is calming, nuturing, supportive and welcoming.
Our Physiotherapists and Occupational Therapists assess, treat and provide education for people who are at risk of or who have lymphoedema. This is often as a result of treatment for cancer. We provide pre-operative and post-operative management and cancer rehabilitation in our Pilates studio. Our team also consists of Physiotherapists who have a strong interest in pelvic floor and continence management for both men and women.

Target Market(s)

Mainly women health conscious

Industry/Entity Type

Allied Health: Physiotherapy / Occupational Therapy

Contact Information for Business Card

Address: 14 Calloway Ave Seabrook 3208 Phone: 84317560 fax: 8431 7564 Email: info@blossomcarepartners.com.au Website: blossomcarepartners.com.au Facebook address: facebook.com/BlossomLymphoedemaAndWomensCareCentre. Room to write appointments. Individual cards need to have name, office email and individual email and professional details

Requirements
Must have
• Logo as per uploaded documents

```html
<!DOCTYPE html>
<html lang="en">
<head>
<meta charset="utf-8">
<title>Blossom – Business Cards</title>
<link href="https://fonts.googleapis.com/css2?family=Arvo:wght@400;700&family=Allura&display=swap" rel="stylesheet">
<style>
  :root{
    --peach:#f7ab7e;
    --sage:#b9c7ba;
    --ink:#474747;
    --paper:#ffffff;
    --backdrop:#2b2b2b;
  }
  *{box-sizing:border-box;margin:0;padding:0}
  html,body{width:1200px;height:900px;overflow:hidden}
  body{background:var(--backdrop);font-family:'Arvo',serif;color:var(--ink);position:relative}

  .card{position:absolute;left:280px;width:640px;height:390px;border-radius:22px;background:var(--paper);overflow:hidden}
  .card--appointment{top:40px}
  .card--profile{top:470px}

  /* appointment card */
  .brand-panel{position:absolute;left:0;top:0;width:250px;height:100%;background:var(--peach);border-right:5px solid var(--sage);display:flex;align-items:center;justify-content:center;gap:10px}
  .brand-mark{width:18px;height:18px;border-radius:50%;background:var(--paper)}
  .brand-name{font-family:'Arvo',serif;font-size:36px;color:var(--paper)}

  .appointment{position:absolute;left:295px;top:48px;right:40px}
  .appointment__title{font-weight:700;font-size:30px;color:var(--peach);margin-bottom:40px}
  .field{display:flex;align-items:flex-end;gap:10px;font-size:15px;margin-bottom:26px}
  .field__line{flex:1;border-bottom:1px dashed #555;height:1px}
  .appointment__rule{position:absolute;left:295px;right:0;top:272px;height:3px;background:var(--sage)}
  .appointment__book{position:absolute;right:40px;top:290px;font-weight:700;font-size:22px;color:var(--peach)}
  .appointment__url{position:absolute;right:40px;top:330px;font-size:15px}

  /* profile card */
  .profile-brand{position:absolute;right:48px;top:36px;display:flex;align-items:center;gap:10px}
  .profile-brand .brand-mark{background:var(--peach)}
  .profile-brand .brand-name{color:var(--peach);font-size:38px}

  .person{position:absolute;left:44px;top:84px}
  .person__name{font-family:'Allura',cursive;font-size:58px;color:var(--peach);line-height:1}
  .person__roles{margin-top:6px;font-size:14px;line-height:1.35}

  .contacts{position:absolute;left:44px;top:222px;list-style:none;font-size:14px;line-height:1.45}
  .contacts li{display:flex;align-items:center;gap:10px}
  .contacts svg{width:14px;height:14px;flex:none;fill:var(--peach)}
  .contacts .dot{width:11px;height:11px;margin:0 1.5px;border-radius:50%;background:var(--peach);flex:none}
</style>
</head>
<body>

<section class="card card--appointment">
  <div class="brand-panel">
    <span class="brand-mark"></span>
    <span class="brand-name">Blossom</span>
  </div>
  <div class="appointment">
    <h2 class="appointment__title">Next Appointment</h2>
    <div class="field"><span>Name:</span><span class="field__line"></span></div>
    <div class="field"><span>Date:</span><span class="field__line"></span></div>
    <div class="field"><span>Time:</span><span class="field__line"></span></div>
  </div>
  <div class="appointment__rule"></div>
  <p class="appointment__book">Book Online</p>
  <p class="appointment__url">blossomcarepartners.com.au</p>
</section>

<section class="card card--profile">
  <div class="profile-brand">
    <span class="brand-mark"></span>
    <span class="brand-name">Blossom</span>
  </div>

  <div class="person">
    <h1 class="person__name">Maren Ashby</h1>
    <p class="person__roles">Physiotherapist<br>Lymphoedema &amp; Oncology Rehabilitation<br>Continence &amp; Pelvic Floor</p>
  </div>

  <ul class="contacts">
    <li><svg viewBox="0 0 24 24"><path d="M6.6 10.8a15 15 0 0 0 6.6 6.6l2.2-2.2c.3-.3.7-.4 1-.2 1.1.4 2.3.6 3.6.6.6 0 1 .4 1 1V20c0 .6-.4 1-1 1A17 17 0 0 1 3 4c0-.6.4-1 1-1h3.5c.6 0 1 .4 1 1 0 1.3.2 2.5.6 3.6.1.3 0 .7-.2 1z"/></svg>84317560 Phone</li>
    <li><svg viewBox="0 0 24 24"><path d="M6 2h12v6H6zM3 9h18v9h-3v4H6v-4H3zm5 7v4h8v-4z"/></svg>8431 7564 Fax</li>
    <li><svg viewBox="0 0 24 24"><path d="M2 4h20v16H2zm2 2v.5l8 6 8-6V6zm0 3v9h16V9l-8 6z"/></svg>maren@blossomcarepartners.com.au</li>
    <li><svg viewBox="0 0 24 24"><path d="M2 4h20v16H2zm2 2v.5l8 6 8-6V6zm0 3v9h16V9l-8 6z"/></svg>info@blossomcarepartners.com.au (office)</li>
    <li><svg viewBox="0 0 24 24"><path d="M12 2a10 10 0 1 0 0 20 10 10 0 0 0 0-20zm6.9 9h-3a15 15 0 0 0-1.4-6 8 8 0 0 1 4.4 6zM12 4c.9 1.3 1.7 3.9 1.9 7h-3.8C10.3 7.9 11.1 5.3 12 4zM9.5 5a15 15 0 0 0-1.4 6h-3a8 8 0 0 1 4.4-6zm-4.4 8h3a15 15 0 0 0 1.4 6 8 8 0 0 1-4.4-6zm6.9 7c-.9-1.3-1.7-3.9-1.9-7h3.8c-.2 3.1-1 5.7-1.9 7zm2.5-1a15 15 0 0 0 1.4-6h3a8 8 0 0 1-4.4 6z"/></svg>blossomcarepartners.com.au</li>
    <li><svg viewBox="0 0 24 24"><path d="M12 3 2 12h3v8h5v-5h4v5h5v-8h3z"/></svg>14 Calloway Ave, Seabrook 3208</li>
    <li><span class="dot"></span>facebook.com/BlossomLymphoedemaAndWomensCareCentre</li>
  </ul>
</section>

</body>
</html>
```